Professional, Upmarket, Gas Station Card Design for a Company

Design for a 2-sided Fuel Card for Vantro Service Stations
Front Design
Has the Vantro Logo and Company Logo
Will have the Card Numbers display
Will have Vehicle Rego Display
Will have Expiry Date

Back Design
Will have a magnetic strip at the bottom of the card
will have a list of service stations the card is valid
will have address of return should the card be lost and found

The card should be blue in color - Vantro Blue
Should have a faded motif design of water droplet

Target Market(s)

Corporate Clients

Industry/Entity Type

Oil and Gas

Font styles to use
Serif

Colors
0054AA
0677BA
7BADD7
CADEEF
E8F1F8

Requirements
Must have
• Vantro Logo, KelFuel Logo, Motif, Magnetic strips
Nice to have
• black color alternative, faded card, traditional design motif, water motif

```html
<!DOCTYPE html>
<html lang="en">
<head>
<meta charset="utf-8">
<title>Vantro Fuel Card – Front and Back</title>
<link rel="stylesheet" href="https://fonts.googleapis.com/css2?family=Roboto:wght@400;500;700;900&family=Roboto+Condensed:wght@400&display=swap">
<style>
  :root {
    --page-bg: #ffffff;
    --vantro-navy: #0d4a94;
    --card-light: #a9c5f3;
    --card-mid: #3f74e2;
    --card-deep: #1a3fcb;
    --card-night: #08168c;
    --sheen: rgba(255, 255, 255, 0.14);
    --ink-white: #ffffff;
    --ink-soft: rgba(255, 255, 255, 0.8);
    --emblem-white: #ffffff;
    --emblem-ink: #b3122a;
    --stripe-black: #050505;
  }

  * { margin: 0; padding: 0; box-sizing: border-box; }

  html, body {
    width: 1200px;
    height: 559px;
    overflow: hidden;
    background: var(--page-bg);
  }

  .sheet {
    position: relative;
    width: 1200px;
    height: 559px;
    font-family: "Roboto", Arial, sans-serif;
  }

  .card {
    position: absolute;
    top: 117px;
    width: 492px;
    height: 296px;
    border-radius: 26px;
    overflow: hidden;
  }

  .card--front { left: 67px; }
  .card--back { left: 653px; }

  .card-motif {
    position: absolute;
    inset: 0;
  }

  .card--front .card-motif {
    background:
      radial-gradient(ellipse 55% 45% at 30% 40%, rgba(120, 165, 240, 0.45), transparent 70%),
      linear-gradient(62deg,
        var(--card-light) 0%,
        #6f97ea 25%,
        var(--card-mid) 45%,
        var(--card-deep) 65%,
        var(--card-night) 88%);
  }

  .card--back .card-motif {
    background:
      radial-gradient(ellipse 40% 50% at 40% 35%, rgba(110, 160, 245, 0.4), transparent 70%),
      linear-gradient(100deg,
        #4f88ec 0%,
        #2d66e2 40%,
        var(--card-deep) 70%,
        var(--card-night) 100%);
  }

  .card-sheen {
    position: absolute;
    inset: 0;
    pointer-events: none;
  }

  .card--back .card-sheen {
    background: linear-gradient(125deg, var(--sheen) 0%, var(--sheen) 42%, transparent 42.2%);
  }

  .card--front .card-sheen {
    background: linear-gradient(118deg, transparent 70%, rgba(0, 0, 60, 0.18) 70.2%);
  }

  .brand-name {
    position: absolute;
    left: 52px;
    top: 18px;
    font-size: 37px;
    font-weight: 900;
    letter-spacing: -1px;
    color: var(--vantro-navy);
  }

  .partner-emblem {
    position: absolute;
    width: 90px;
    height: 90px;
    border-radius: 50%;
    background: var(--emblem-white);
    display: flex;
    align-items: center;
    justify-content: center;
    font-size: 16px;
    font-weight: 700;
    color: var(--emblem-ink);
  }

  .card--front .partner-emblem { left: 360px; top: 26px; }
  .card--back .partner-emblem { left: 210px; top: 18px; }

  .card-number {
    position: absolute;
    left: 51px;
    top: 139px;
    font-family: "Roboto Condensed", "Arial Narrow", sans-serif;
    font-size: 42px;
    letter-spacing: 0.6px;
    word-spacing: 4px;
    color: var(--ink-white);
    white-space: nowrap;
  }

  .vehicle-rego {
    position: absolute;
    left: 50px;
    top: 210px;
    font-size: 16px;
    color: var(--ink-soft);
  }

  .expiry {
    position: absolute;
    left: 330px;
    top: 212px;
    display: flex;
    align-items: center;
    gap: 5px;
    color: var(--ink-white);
  }

  .expiry-label {
    font-size: 14px;
    line-height: 14px;
  }

  .expiry-date {
    font-family: "Roboto Condensed", "Arial Narrow", sans-serif;
    font-size: 20px;
  }

  .cardholder {
    position: absolute;
    left: 50px;
    top: 250px;
    font-size: 20px;
    color: var(--ink-white);
    white-space: nowrap;
  }

  .card-terms {
    position: absolute;
    left: 58px;
    top: 130px;
    width: 398px;
    color: var(--ink-soft);
    font-size: 6px;
    line-height: 8.5px;
  }

  .card-terms p + p { margin-top: 6px; }

  .magnetic-stripe {
    position: absolute;
    left: 0;
    top: 190px;
    width: 100%;
    height: 70px;
    background: var(--stripe-black);
  }
</style>
</head>
<body>
<main class="sheet">

  <section class="card card--front" aria-label="Fuel card front">
    <div class="card-motif" role="img" aria-label="Faded water droplet motif in Vantro blue"></div>
    <div class="card-sheen" aria-hidden="true"></div>
    <div class="brand-name">Vantro</div>
    <div class="partner-emblem">KelFuel</div>
    <div class="card-number">1234 5678 9012 3456</div>
    <div class="vehicle-rego">GVR223</div>
    <div class="expiry">
      <span class="expiry-label">VALID<br>THRU</span>
      <svg width="6" height="8" viewBox="0 0 6 8" aria-hidden="true"><path d="M0 0 L6 4 L0 8 Z" fill="#ffffff"/></svg>
      <span class="expiry-date">01/24</span>
    </div>
    <div class="cardholder">CARDHOLDER NAME</div>
  </section>

  <section class="card card--back" aria-label="Fuel card back">
    <div class="card-motif" role="img" aria-label="Faded water droplet motif in Vantro blue"></div>
    <div class="card-sheen" aria-hidden="true"></div>
    <div class="partner-emblem">KelFuel</div>
    <div class="card-terms">
      <p>Valid at all Vantro and KelFuel service stations across the network. If found, please return this card to Vantro Fleet Services, 14 Harbour Road, Port Elden 4021. Card remains company property.</p>
      <p>Use of this card is subject to the fleet account terms. Report loss or theft immediately to your account manager. Fuel purchases are billed monthly to the registered corporate account holder.</p>
    </div>
    <div class="magnetic-stripe"></div>
  </section>

</main>
</body>
</html>
```